Business Card Design - Pediatric Dentist

We need a business card for a new dental office. We are a pediatric dentist in Austin Tx. I would like a design that use bright green and if possible light blue.

Target Market(s)

Marketed to young moms

Industry/Entity Type

Dental

Contact Information for Business Card

Marcus Pell DDS
Bramblewood Family Dentistry
428 E. Marlowe Road. Austin TX 78690
(512) 555 0183.

In the back i would like to state "we take most insurances, Tova & Vitacover" & a map

Colors
add136
cadf82
85cae6

```html
<!DOCTYPE html>
<html lang="en">
<head>
<meta charset="utf-8">
<title>Bramblewood Family Dentistry – Business Card</title>
<link rel="stylesheet" href="https://fonts.googleapis.com/css2?family=Tinos&family=Asap+Condensed:wght@700&display=swap">
<style>
  :root {
    --card-green: #cadf82;
    --edge-blue: #85cae6;
    --mark-green: #2e9e3f;
    --ink: #111111;
    --name-ink: #0c1a36;
    --name-glow: #85cae6;
    --panel: #fefefe;
    --page: #ffffff;
  }
  html, body {
    margin: 0;
    padding: 0;
    width: 1200px;
    height: 702px;
    overflow: hidden;
    background: var(--page);
  }
  .card {
    position: relative;
    width: 1200px;
    height: 702px;
    font-family: "Tinos", "Times New Roman", serif;
    color: var(--ink);
  }
  .card-shape {
    position: absolute;
    inset: 0;
  }
  .brand-mark {
    position: absolute;
    left: 118px;
    top: 102px;
    width: 230px;
    height: 230px;
    border-radius: 50%;
    background: var(--mark-green);
  }
  .brand-name {
    position: absolute;
    left: 370px;
    top: 116px;
    margin: 0;
    font-weight: 400;
    font-size: 58px;
    line-height: 76px;
    color: var(--ink);
  }
  .dentist-name {
    position: absolute;
    left: 739px;
    top: 106px;
    margin: 0;
    font-family: "Asap Condensed", "Arial Narrow", sans-serif;
    font-weight: 700;
    font-size: 64px;
    line-height: 1;
    color: var(--name-ink);
    text-shadow:
      -2px -2px 0 var(--name-glow), 2px -2px 0 var(--name-glow),
      -2px 2px 0 var(--name-glow), 2px 2px 0 var(--name-glow),
      0 0 12px var(--name-glow);
  }
  .contact {
    position: absolute;
    left: 741px;
    top: 200px;
    margin: 0;
    font-style: normal;
    font-size: 24px;
    line-height: 40px;
  }
  .contact .phone { display: block; margin-top: 6px; }
  .note-panel {
    position: absolute;
    left: 123px;
    top: 448px;
    width: 988px;
    height: 153px;
    background: var(--panel);
    border-radius: 14px;
    display: flex;
  }
  .note-field {
    flex: 1;
    text-align: center;
    font-size: 24px;
    padding-top: 8px;
  }
  .note-field + .note-field {
    border-left: 3px solid var(--ink);
    padding-top: 5px;
  }
</style>
</head>
<body>
  <main class="card">
    <svg class="card-shape" width="1200" height="702" viewBox="0 0 1200 702" aria-hidden="true">
      <polygon points="61,58 76,74 76,633 1147,633 1147,648 61,648" fill="var(--edge-blue)"/>
      <polygon points="61,58 1144,58 1144,633 76,633 76,74" fill="var(--card-green)"/>
    </svg>

    <div class="brand-mark" aria-hidden="true"></div>
    <h1 class="brand-name">Bramblewood<br>Family<br>Dentistry</h1>

    <h2 class="dentist-name">Marcus Pell</h2>
    <address class="contact">
      DDS Bramblewood Family Dentistry<br>
      428 E. Marlowe Road.<br>
      Austin TX 78690<br>
      <span class="phone">Ph:(512) 555 0183</span>
    </address>

    <section class="note-panel">
      <div class="note-field">Next Appointment</div>
      <div class="note-field">Important Date/Number</div>
    </section>
  </main>
</body>
</html>
```